Business card and (possibly) logo

Hi - we need a new business card.
We have an existing logo that we quite like but we are open to options.
We are an architectural firm - we specialize in upmarket residential work and apartment blocks.
We are chasing a business card at present but also want to extensively update our website going forward to attract a much higher level of client / investor / developer.
Our current logo is black, grey and yellow and based on the sun/moon temples in Mexico.
We are open to variations.
We want to communicate professionalism, trust, quality.
Our website is www.corvelldesignhouse.com.au - but note as above - we want to change the website as well to be a lot 'classier' and to appeal to a higher end market.

thanks

Target Market(s)

We are an architect firm - our target market is Developers and builders of high end houses and luxury apartment blocks. Also private home owners wanting to build excellent expensive houses. (ideally over $1m budgets)

Industry/Entity Type

Residential

Requirements
Must have
• Logo
Contact details;
Name
phone, mobile, email, web

```html
<!DOCTYPE html>
<html lang="en">
<head>
<meta charset="utf-8">
<title>Corvell Design House – Business Card</title>
<link rel="stylesheet" href="https://fonts.googleapis.com/css2?family=Bebas+Neue&display=swap">
<style>
  :root {
    --ink: #000000;
    --paper: #ffffff;
    --teal: #12a2b8;
    --ghost: #e4e4e4;
    --display: "Bebas Neue", "Arial Narrow", sans-serif;
    --body: Arial, Helvetica, sans-serif;
  }
  * { margin: 0; padding: 0; box-sizing: border-box; }
  html, body {
    width: 1200px; height: 1000px; overflow: hidden;
    background: var(--paper);
  }
  .canvas { position: relative; width: 1200px; height: 1000px; }

  .card {
    position: absolute;
    left: 74px;
    width: 728px;
    border: 3px solid var(--ink);
    border-radius: 3px;
    background: var(--paper);
    overflow: hidden;
  }

  /* Front */
  .card--front { top: 30px; height: 458px; }
  .front__base {
    position: absolute; left: 0; right: 0; top: 264px; bottom: 0;
    background: var(--ink);
  }
  .front__name {
    position: absolute; left: 0; right: 0; top: 132px;
    text-align: center;
    font-family: var(--display);
    font-size: 164px; line-height: 1;
    letter-spacing: 6px;
    color: var(--ink);
  }

  /* Back */
  .card--back { top: 516px; height: 457px; }
  .back__rule {
    position: absolute; left: 0; right: 0; top: 72px;
    height: 3px; background: var(--ink);
  }
  .back__name {
    position: absolute; left: 52px; top: 14px;
    font-family: var(--display);
    font-size: 72px; line-height: 1;
    letter-spacing: 3px;
    color: var(--ink);
  }
  .back__watermark {
    position: absolute; left: 232px; top: 148px;
    font-family: var(--display);
    font-size: 240px; line-height: 1;
    letter-spacing: 30px;
    color: var(--ghost);
    white-space: nowrap;
  }
  .person {
    position: absolute; left: 32px; top: 134px;
  }
  .person__name {
    font-family: var(--display);
    font-size: 70px; line-height: 1;
    color: var(--ink);
    margin-bottom: 8px;
  }
  .person__contact {
    list-style: none;
    font-family: var(--body);
    font-size: 17px; line-height: 23.5px;
    color: var(--ink);
  }
  .tagline-band {
    position: absolute; left: 0; right: 0; bottom: 0; height: 110px;
    background: var(--teal);
  }
  .tagline {
    position: absolute; left: 46px; top: 30px;
    font-family: var(--body);
    font-style: italic;
    font-size: 41px;
    color: var(--paper);
  }
</style>
</head>
<body>
<main class="canvas">
  <section class="card card--front" aria-label="Card front">
    <div class="front__name">CORVELL</div>
    <div class="front__base"></div>
  </section>

  <section class="card card--back" aria-label="Card back">
    <div class="back__watermark" aria-hidden="true">CORVELL</div>
    <div class="back__name">CORVELL</div>
    <div class="back__rule"></div>
    <div class="person">
      <h1 class="person__name">MARA LINDQVIST</h1>
      <ul class="person__contact">
        <li>+0917845120</li>
        <li>mara@corvellmail.com</li>
        <li>www.corvelldesignhouse.com.au</li>
      </ul>
    </div>
    <div class="tagline-band">
      <p class="tagline">tag line here</p>
    </div>
  </section>
</main>
</body>
</html>
```